Gutschein-Design für Apotheken
Zielgruppe
Unsere Familie betreibt 4 Apotheken in Bayern.
Diese haben seit kurzem die Dachmarke und dem CI 'Lerchen-Apotheken', sind aber alle weiter unter eigenem Namen eigenständig.
Unsere Kunden erhalten als Dankeschön für den Besuch einen netten Prämienkäfer, der dann gegen schöne Dinge eingetauscht werden kann.
Wir suchen einen neuen Gutschein für unsere Kunden, der in allen Apotheken von uns erworben werden kann und auch überall eingelöst werden kann.
Bisher hatte jede Apotheke einzelne Gutscheine. Die Apotheke Am Lindenhof hat zusätzlich noch einen reinen Kosmetikgutschein, der für Behandlungen etc. ausgegeben wird.
Nun suchen wir einen neuen Gutschein, in dem der Barwert (z.B. 40€) eingetragen wird und der für alles (Arzneimittel, Bonbons etc.) und überall eingelöst werden kann.
Ziel: gemeinsamer Gutschein für Kunden
Format: bevorzugt wie Kosmetikgutschein, gerne aber auch andere Ideen erwünscht (Gutscheinkarte in dem Format, dafür hinten und vorne Info?)
BITTE MODERNES DESIGN, kein klassisches, altbackenes Design von Apotheken (Blümchen etc.)
Inhalt: nicht wirklich viel:
- Gutschein über
- Leerzeichen wo Betrag eingetragen wird
- Gutscheinnummer; Leerzeichen, wo Nummer eingetragen wird
- Datum Unterschrift
- Information, dass dieser Gutschein in allen unseren Apotheken eingelöst werden kann.
- keine Gültigkeit! (Kunden können den Gutschein unendlich lang einlösen bei uns)
- irgend ein netter Spruch? 'Gesundheit ist alles' o.ä 'Gesundheit schenken'... ?!
- evtl. nettes Bild / Gesundheit etc.
- Logos und Adressen von allen 4 Apotheken
- GERNE Käfer mit einbauen (ist unser Wiedererkennungswert! )
(Achtung: 3x Wendlinger Apotheken haben einen technischen Käfer, Apotheke Hornau hat einen anderen. Ist aber ok so!)
Anbei Beispiele von Flyern, wo wir halbprofessionell schon alle 4 Apotheken mit auf den Flyer tun.
An..
Aufgabenstellung
siehe Anhang

```html
<!DOCTYPE html>
<html lang="de">
<head>
<meta charset="utf-8">
<title>Gutschein – Lerchen-Apotheken</title>
<link rel="stylesheet" href="https://fonts.googleapis.com/css2?family=Great+Vibes&family=Michroma&family=Poppins:wght@400;600&display=swap">
<style>
  :root {
    --bg: #d9d9d9;
    --paper: #ffffff;
    --red: #e32131;
    --red-dark: #b5121e;
    --ink: #1a1a1a;
    --grey: #555555;
    --script: #f4f4f4;
    --photo-skin: #e9c9b4;
    --photo-green: #a9c173;
  }
  html, body { margin: 0; padding: 0; }
  body {
    width: 1200px; height: 2200px; overflow: hidden;
    background: var(--bg);
    position: relative;
    font-family: "Poppins", sans-serif;
    color: var(--ink);
  }
  .spread {
    position: absolute; left: 30px;
    width: 1140px; height: 286px;
    background: var(--paper);
    overflow: hidden;
    box-shadow: 0 6px 18px rgba(0,0,0,.18);
  }
  .spread--outside { top: 800px; }
  .spread--inside { top: 1140px; }

  .band {
    position: absolute; left: 0; right: 0; top: 229px; height: 43px;
    background: var(--red);
  }
  .bow {
    position: absolute;
    background: radial-gradient(ellipse at center, var(--red-dark) 0%, var(--red) 45%, rgba(227,33,49,0) 72%);
  }
  .ladybug {
    position: absolute; border-radius: 50%;
    background: radial-gradient(circle at 40% 40%, #ef3a3a 0%, #d51e24 70%, #a0141a 100%);
  }

  /* outside: back panel */
  .pharmacy {
    position: absolute; top: 130px; width: 128px;
    font-size: 7px; line-height: 1.45; color: var(--ink);
  }
  .pharmacy__name {
    display: flex; align-items: center; gap: 4px;
    font-size: 10px; font-weight: 600; text-transform: uppercase;
    line-height: 1.1; margin-bottom: 6px; height: 24px;
  }
  .pharmacy__mark { width: 9px; height: 9px; background: var(--ink); flex: none; }
  .url {
    position: absolute; left: 26px; top: 227px;
    font-size: 34px; font-weight: 600; color: var(--paper); letter-spacing: .5px;
  }

  /* outside: front panel */
  .photo {
    position: absolute; left: 593px; top: 20px; width: 404px; height: 176px;
    background: linear-gradient(90deg, var(--photo-green) 0%, var(--photo-skin) 30%, var(--photo-skin) 80%, #d9c3ad 100%);
  }
  .slogan {
    position: absolute; left: 900px; top: 70px;
    font-family: "Michroma", sans-serif; font-size: 29px; line-height: 1.35;
    color: var(--paper); font-weight: 400;
    text-shadow: 2px 2px 3px rgba(0,0,0,.45);
    margin: 0;
  }

  /* inside: left panel */
  .title {
    position: absolute; left: 40px; top: 0;
    font-family: "Great Vibes", cursive; font-size: 150px; line-height: 1;
    color: var(--script); margin: 0; font-weight: 400;
    text-shadow: 2px 3px 4px rgba(0,0,0,.35);
  }
  .recipient {
    position: absolute; left: 128px; top: 206px; width: 360px;
    font-size: 12px; color: var(--grey);
    display: flex; align-items: baseline; gap: 4px;
  }
  .dots { flex: 1; border-bottom: 1px dotted #888; }

  /* inside: right panel */
  .field {
    position: absolute; left: 646px; width: 486px;
    font-size: 11px; color: var(--grey);
    display: flex; align-items: baseline; gap: 4px;
  }
  .field--value { top: 30px; }
  .field--date { top: 98px; }
  .field--number { top: 172px; }
  .field__line { position: absolute; left: 646px; top: 108px; width: 486px; border-bottom: 1px dotted #888; }
  .field--date .gap { width: 130px; }
  .redeem {
    position: absolute; left: 784px; top: 244px;
    font-size: 10px; color: var(--paper); font-weight: 600; margin: 0;
  }
</style>
</head>
<body>

<section class="spread spread--outside" aria-label="Gutschein Außenseite">
  <div class="band"></div>

  <div class="ladybug" role="img" aria-label="Kleiner Marienkäfer" style="left:88px;top:26px;width:38px;height:34px;"></div>
  <div class="ladybug" role="img" aria-label="Kleiner Marienkäfer" style="left:150px;top:68px;width:28px;height:26px;"></div>
  <div class="ladybug" role="img" aria-label="Kleiner Marienkäfer" style="left:46px;top:208px;width:22px;height:22px;"></div>
  <div class="ladybug" role="img" aria-label="Marienkäfer am Falz" style="left:570px;top:96px;width:44px;height:48px;"></div>

  <div class="pharmacy" style="left:22px;">
    <div class="pharmacy__name"><span class="pharmacy__mark"></span>Apotheke Am Lindenhof</div>
    Lindenweg 6 - 73240 Wendlingen<br>Tel: 07024 / 5530-0 - Fax: 5530-20<br>lindenhof@lerchen-apotheken.de
  </div>
  <div class="pharmacy" style="left:158px;">
    <div class="pharmacy__name"><span class="pharmacy__mark"></span>Apotheke am Steintor</div>
    Am Steintor 1 - 73240 Wendlingen<br>Tel: 07024 / 41862 - Fax: 41863<br>steintor@lerchen-apotheken.de
  </div>
  <div class="pharmacy" style="left:293px;">
    <div class="pharmacy__name"><span class="pharmacy__mark"></span>quellplus apotheke</div>
    Quellgasse 15 - 73240 Wendlingen<br>Tel: 07024 / 9380210 - Fax: 9380211<br>quellplus@lerchen-apotheken.de
  </div>
  <div class="pharmacy" style="left:428px;">
    <div class="pharmacy__name"><span class="pharmacy__mark"></span>Apotheke Am Lindenhof</div>
    Lindenweg 6 - 73240 Wendlingen<br>Tel: 07024 / 5530-0 - Fax: 5530-20<br>lindenhof@lerchen-apotheken.de
  </div>

  <div class="url">www.lerchen-apotheken.de</div>

  <div class="photo" role="img" aria-label="Foto: Hände formen ein Herz auf dem Bauch"></div>
  <p class="slogan">Gesundheit<br>schenken!</p>
  <div class="ladybug" role="img" aria-label="Marienkäfer" style="left:1026px;top:0;width:58px;height:52px;"></div>
  <div class="ladybug" role="img" aria-label="Kleiner Marienkäfer" style="left:1112px;top:120px;width:24px;height:24px;"></div>
  <div class="bow" role="img" aria-label="Rote Geschenkschleife" style="left:600px;top:200px;width:270px;height:86px;"></div>
  <div class="ladybug" role="img" aria-label="Großer Marienkäfer" style="left:922px;top:176px;width:180px;height:140px;"></div>
</section>

<section class="spread spread--inside" aria-label="Gutschein Innenseite">
  <div class="band"></div>

  <div class="ladybug" role="img" aria-label="Großer Marienkäfer" style="left:-40px;top:-40px;width:160px;height:120px;"></div>
  <h1 class="title">Gutschein</h1>
  <div class="ladybug" role="img" aria-label="Kleiner Marienkäfer" style="left:462px;top:62px;width:26px;height:28px;"></div>
  <div class="ladybug" role="img" aria-label="Kleiner Marienkäfer" style="left:552px;top:162px;width:34px;height:38px;"></div>
  <div class="recipient">für <span class="dots"></span></div>
  <div class="bow" role="img" aria-label="Rote Geschenkschleife" style="left:440px;top:205px;width:320px;height:86px;"></div>

  <div class="ladybug" role="img" aria-label="Marienkäfer" style="left:600px;top:58px;width:44px;height:46px;"></div>
  <div class="field field--value">im Wert von <span class="dots" style="flex:0 0 60px"></span> Euro in Worten <span class="dots"></span></div>
  <div class="field__line"></div>
  <div class="field field--date">Datum <span class="gap"></span> Stempel / Unterschrift</div>
  <div class="field field--number">Gutschein Nr. <span class="dots"></span></div>
  <p class="redeem">Einzulösen in allen Lerchen-Apotheken</p>
  <div class="ladybug" role="img" aria-label="Großer Marienkäfer" style="left:1000px;top:186px;width:150px;height:120px;"></div>
</section>

</body>
</html>
```